Business card design needed

Our company background is that we provides transfers to and from the airport, social & corporate events, weddings.
We are also available for charter for birthday party, wine tastings, concerts, anniversary, school balls etc.
Our business cards have to reflect that we have a professional company, they are our first contact and have to stand out from the other 'players' in the market.

Industry/Entity Type

School

Contact Information for Business Card

VESTAR PTH, Teodor & Marguerite, mob: 0427 381 592, PO Box 284, Corran Bay KV 4172, ABN 52 614 203 178, Lic 7169/2058,

Requirements
Must have
• Telephone number: 0427 381 592
Website: www.VESTARPTH.com.au
postal address: PO Box 284, Corran Bay KV 4172
Licences: Lic 7169/2058

***If using the new photo (one with the bus and buildings behind it), if possible can the buildings be cropped out. Thanks
Nice to have
• would be nice to have the pics of the vehicle(s), preferred the Vel on the card but not too fussed.
Should not have
• Picture of vehicle we don't have in our fleet. (We ONLY have the Velarions and Murako Densa mini bus)

```html
<!DOCTYPE html>
<html lang="en">
<head>
<meta charset="utf-8">
<title>VESTAR PTH – Business Card</title>
<link rel="stylesheet" href="https://fonts.googleapis.com/css2?family=Vollkorn:wght@600;700;800&display=swap">
<style>
  :root {
    --backdrop: #3b3b3b;
    --card: #070606;
    --band: #8b7f7b;
    --band-edge: #aa9e99;
    --ink: #1b1414;
    --logo: #928682;
    --vehicle-light: #c9c1b6;
    --vehicle-dark: #6f6a64;
  }
  * { margin: 0; padding: 0; box-sizing: border-box; }
  html, body {
    width: 1200px;
    height: 900px;
    overflow: hidden;
    background: var(--backdrop);
    font-family: "Vollkorn", Georgia, serif;
    font-variant-numeric: lining-nums;
  }
  .stage { position: relative; width: 1200px; height: 900px; }

  .card {
    position: absolute;
    top: 303px;
    width: 525px;
    height: 294px;
    background: var(--card);
  }
  .card--front { left: 58px; }
  .card--back { left: 617px; }

  .brand {
    position: absolute;
    top: 106px;
    width: 212px;
    text-align: center;
    color: var(--logo);
    font-weight: 800;
    line-height: 1;
  }
  .card--front .brand { left: 32px; }
  .card--back .brand { left: 282px; }
  .brand__name { display: block; font-size: 44px; letter-spacing: 1px; }
  .brand__suffix { display: block; font-size: 22px; margin-top: 2px; letter-spacing: 2px; }

  .band {
    position: absolute;
    top: 92px;
    height: 110px;
    background: var(--band);
    border: 2px solid var(--band-edge);
  }
  .card--front .band { left: 273px; width: 252px; border-right: none; }
  .card--back .band { left: 0; width: 250px; border-left: none; }

  .vehicle-photo {
    position: absolute;
    left: 20px;
    top: 6px;
    width: 212px;
    height: 94px;
    border-radius: 30px 40px 8px 8px;
    background: linear-gradient(180deg, var(--vehicle-light) 0%, var(--vehicle-dark) 100%);
  }

  .contact { padding: 13px 0 0 20px; color: var(--ink); }
  .contact__names { font-size: 20px; font-weight: 800; margin-bottom: 5px; white-space: nowrap; }
  .contact__line { font-size: 11.5px; font-weight: 700; line-height: 15px; white-space: nowrap; }
  .contact__line--mobile { font-size: 14px; margin-bottom: 3px; }
</style>
</head>
<body>
<main class="stage">
  <section class="card card--front" aria-label="Business card front">
    <div class="brand">
      <span class="brand__name">VESTAR</span>
      <span class="brand__suffix">PTH</span>
    </div>
    <div class="band">
      <div class="vehicle-photo" role="img" aria-label="Photo of a silver Velarion sedan"></div>
    </div>
  </section>

  <section class="card card--back" aria-label="Business card back">
    <div class="band">
      <div class="contact">
        <p class="contact__names">Teodor &amp; Marguerite</p>
        <p class="contact__line contact__line--mobile">mob: 0427 381 592</p>
        <p class="contact__line">PO Box 284, Corran Bay KV 4172,</p>
        <p class="contact__line">ABN 52 614 203 178, Lic 7169/2058</p>
      </div>
    </div>
    <div class="brand">
      <span class="brand__name">VESTAR</span>
      <span class="brand__suffix">PTH</span>
    </div>
  </section>
</main>
</body>
</html>
```